Hearth & Keg Room requires web site design - Casual restaurant

Need website designed for re-branding of Restaurant based in Fort Morgan, Colorado. We offer a wide variety of American cuisine in a casual, rustic atmosphere. We're offering 16 craft beers on draft, as well as a full service bar, and modern, interesting menu selections in a friendly, fun and energetic environment, with an emphasis on superior customer service and high quality, locally sourced food. We are a family, and community service oriented establishment. The website design should convey a welcoming sense, "simplicity", yet sophisticated - without pretentiousness. The website should effectively convey our "home style" relaxed atmosphere, as well as our casual character.

Business Hours: Sunday - Thursday, 11am-10pm / Friday & Saturday, 11am-11am

The Dunlo Hearth & Keg Room
2736 Pennick Road
Fort Morgan, Colorado 80701
B: (970) 555-0173

WEBSITE ADDRESS: thedunlokegroom.com

Target Market(s)

Young Adults
Families
Blue and White Collar Americans
Senior Citizens
Small town location, appeal to everyone

Industry/Entity Type

American Restaurant

Contact Information for Business Card

Marcus T Ellery
Food & Beverage Director
2736 Pennick Road
B: (970) 555-0173
M: (231) 555-0148
mtellery@dunlokegroom.com
www.thedunlokegroom.com
***Use logo in uploaded files
***Open to single OR double sided
*** I will have additional names and information to add to this, for other employees.

Coding

Coded - Design and coding required

Number of Pages Required

5+ page

Font styles to use
Serif
Sans Serif
Decorative
Other font styles liked:
• Calafornian FB,

Requirements
Must have
• Home/Welcome Page
• Menu Page/Online Ordering Ready
• About Us/Contact Us page
• Catering/Private Events/Banquets Advertising section
• Ability to link to Facebook/TripAdvisor/Yelp/Instagram etc.
• Logo uploaded, reference for colors as well.
Nice to have
• About craft beer page
• Our Story/Bio section
• Photo Gallery
• Employment/Apply section
Should not have
• We are NOT a "fine dining" restaurant... think casual...

```html
<!DOCTYPE html>
<html lang="en">
<head>
<meta charset="utf-8">
<title>The Dunlo Hearth &amp; Keg Room</title>
<link href="https://fonts.googleapis.com/css2?family=Lato:ital,wght@0,300;0,400;0,700;1,400&family=Oswald:wght@300;400&family=Arimo:wght@400;700&display=swap" rel="stylesheet">
<style>
:root{
  --wood:#4a200f;
  --wood-dark:#2e1207;
  --maroon:#4a0000;
  --maroon-deep:#6a0d0a;
  --cream:#f6f3ed;
  --orange:#fb6a09;
  --heading:#6b0f0c;
  --body:#8b8580;
  --ink:#1f1a17;
}
*{box-sizing:border-box;margin:0;padding:0}
html,body{width:1200px;height:1035px;overflow:hidden}
body{
  background:linear-gradient(90deg,var(--wood-dark),var(--wood) 30%,#5a2812 50%,var(--wood) 70%,var(--wood-dark));
  font-family:"Lato",sans-serif;
  position:relative;
}
.site{position:absolute;left:123px;top:0;width:962px;height:1035px;background:var(--cream)}
.topbar{height:48px;background:var(--maroon);display:flex;align-items:center;justify-content:space-between;padding:0 42px 0 44px;color:#fff;font-size:11.5px}
.topbar-right{display:flex;align-items:center;gap:10px}
.order-pill{background:var(--orange);color:#fff;font-weight:700;font-size:10.5px;padding:2px 11px;border-radius:2px;margin-left:4px;margin-right:4px}
.social{display:flex;gap:4px}
.social span{width:24px;height:24px;border:1.5px solid #fff;border-radius:50%;background:#000;display:flex;align-items:center;justify-content:center}
.header{height:121px;position:relative}
.brand{position:absolute;left:60px;top:28px;display:flex;align-items:center;gap:8px;color:var(--ink);font-family:"Lato",sans-serif;font-weight:700}
.brand-mark{width:14px;height:14px;background:var(--maroon-deep)}
.brand-name{font-size:34px;line-height:1}
.brand-tag{font-size:11px;line-height:1.4}
.nav{position:absolute;right:42px;top:55px;display:flex;gap:23px;font-family:"Oswald",sans-serif;font-weight:300;font-size:18px;letter-spacing:2.5px;color:var(--ink);text-transform:uppercase}
.nav a{color:inherit;text-decoration:none;position:relative}
.nav a.active::after{content:"";position:absolute;left:0;right:2px;bottom:-6px;height:2px;background:var(--maroon-deep)}
.hero{height:406px;position:relative;background:radial-gradient(ellipse at 30% 40%,#c08a2a,#6b3a12 45%,#2a1508 80%),#3a1d0a}
.hero-title{position:absolute;left:56px;top:215px;height:56px;padding:0 4px 0 6px;background:rgba(90,8,5,.82);color:#fff;font-family:"Arimo",sans-serif;font-size:48px;line-height:56px;white-space:nowrap}
.hero-title b{font-weight:700}
.hero-sub{position:absolute;left:80px;top:271px;width:633px;height:54px;padding:6px 24px;background:rgba(90,8,5,.82);color:#fff;font-family:"Arimo",sans-serif;font-weight:700;font-size:15px;line-height:23px}
.features{position:relative;height:460px}
.feature{position:absolute;top:46px;width:264px}
.feature:nth-child(1){left:41px}
.feature:nth-child(2){left:347px}
.feature:nth-child(3){left:653px}
.photo-frame{width:264px;height:164px;background:#fff;border:1px solid #e3ded6;padding:7px}
.photo{width:100%;height:100%}
.kicker{margin-top:22px;color:var(--orange);font-style:italic;font-size:13.5px}
.feature h2{margin-top:14px;color:var(--heading);font-weight:400;font-size:25px;letter-spacing:-.3px}
.feature p{margin-top:20px;color:var(--body);font-weight:300;font-size:13.5px;line-height:21px}
.feature p b{font-weight:700}
.btn{position:absolute;top:355px;left:4px;height:32px;padding:0 14px;display:flex;align-items:center;border:1px solid #d9d4cc;background:#fff;color:#555;font-size:11px;letter-spacing:1.3px;text-transform:uppercase}
.btn-primary{background:var(--orange);border-color:var(--orange);color:#fff;font-weight:700}
</style>
</head>
<body>
<div class="site">
  <div class="topbar">
    <div>2736 Pennick Road.Fort Morgan, Colorado 80701
      <svg width="8" height="10" viewBox="0 0 8 10"><path d="M4 0a3.5 3.5 0 0 0-3.5 3.5C.5 6 4 10 4 10s3.5-4 3.5-6.5A3.5 3.5 0 0 0 4 0zm0 5a1.4 1.4 0 1 1 0-2.8A1.4 1.4 0 0 1 4 5z" fill="#fff"/></svg>
    </div>
    <div class="topbar-right">
      <span>Call Us: (970) 555-0173</span>
      <svg width="10" height="10" viewBox="0 0 10 10"><rect width="10" height="10" rx="2" fill="#fff"/><path d="M3 2.5l1 1.2-.6.8a4 4 0 0 0 2 2l.8-.6 1.2 1-.7.9C4.6 7.6 2.4 5.4 2.2 3.3z" fill="#4a0000"/></svg>
      <span class="order-pill">ORDER ONLINE</span>
      <div class="social">
        <span></span><span></span><span></span><span></span>
        <span><svg width="11" height="8" viewBox="0 0 11 8"><rect x=".5" y=".5" width="10" height="7" fill="#fff"/><path d="M.5.5l5 4 5-4" stroke="#000" fill="none"/></svg></span>
      </div>
    </div>
  </div>
  <header class="header">
    <div class="brand">
      <span class="brand-mark"></span>
      <div><div class="brand-name">The Dunlo</div><div class="brand-tag">Hearth &amp; Keg Room</div></div>
    </div>
    <nav class="nav">
      <a class="active">Home</a><a>About Us</a><a>Menu</a><a>Order Online</a><a>Gallery</a><a>Contact</a>
    </nav>
  </header>
  <section class="hero" role="img" aria-label="Warm-lit bar with brass beer taps and shelves of bottles">
    <h1 class="hero-title">The <b>DUNLO</b> Hearth &amp; Keg Room</h1>
    <p class="hero-sub">A lovely place to meet a friend and chat over lunch, served in a pleasant little room with wonderful tacos and handcrafted burgers.</p>
  </section>
  <section class="features">
    <article class="feature">
      <div class="photo-frame"><div class="photo" role="img" aria-label="Chefs in white uniforms at a kitchen station" style="background:linear-gradient(135deg,#2f4a30,#8a8a80 55%,#d8d6d0)"></div></div>
      <div class="kicker">The Executive Chef</div>
      <h2>RENZO CALDER</h2>
      <p>Renzo was honest and smart and had the highest personal integrity of anyone I have ever known about people.</p>
      <a class="btn">View our chefs</a>
    </article>
    <article class="feature">
      <div class="photo-frame"><div class="photo" role="img" aria-label="Restaurant storefront lit up on a street at dusk" style="background:linear-gradient(160deg,#1a2238,#5a2a20 50%,#c0461e 70%,#2a2a2e)"></div></div>
      <div class="kicker">The Best Of Colorado</div>
      <h2>RESTAURANT</h2>
      <p><b>Phone:</b> (970) 555-0173<br><b>Address:</b> 2736 Pennick Road.<br>Fort Morgan, Colorado 80701</p>
      <a class="btn">More about us</a>
    </article>
    <article class="feature">
      <div class="photo-frame"><div class="photo" role="img" aria-label="Friends raising glasses of red wine over a dinner table" style="background:radial-gradient(circle at 45% 45%,#6a2028,#b08a78 55%,#e6ded4)"></div></div>
      <div class="kicker">Premium Dinner Services</div>
      <h2>DINING ROOM</h2>
      <p>The dining room by nature is simple space. Unlike a kitchen or living room, which often has multiple purposes.</p>
      <a class="btn btn-primary">Make a order online »</a>
    </article>
  </section>
</div>
</body>
</html>
```